lunetra.com redesign

We are a successful web hosting company that has been around since 1999 with 10,000 customers managing 2,000 websites and 12,000 domain names. Our challenge - we are losing ground because our site is getting old, our pricing is not competitive and our feature set needs to change to match the new world of mobile centric everything. We want to reach out to all of the domain names that we don't host websites for. We believe that if we designed a new site that focuses on bringing home all of those externally hosted websites to our own web hosting company that we would have a solid future. We need to compete against mopwizzle.com, vantrimble.com, kerbloom.com, zinqhut.com, nolvark.com, brimfolk.com, quorvane.com, welbix.com and 100,000 others. We need to simplify our message with clean design, focused pages, easy decision making processes for the consumer. We use WHMCS for the background provisioning and billing so we can pretty much manage any kind of pricing model and discounted promotion packages.
I would prefer Twitter bootstrap CSS based responsive design.

Reason: I was away on vacation for 2 weeks - I just got back - I need time to fairly review all submissions - thank you for your patience. Dorian Fenwick Lunetra.com

Thanks to all who submitted sample designs - unfortunately most of them were nothing much more than already available templates with some of my current content and logo added to them. I will try to be more specific to reduce the number of choices. I need the template be fully compatible with WHMCS and Wordpress if you can't make it work with WHMCS directly. Another question I have to ask is -"exactly what am I getting for my $500.00 - is it just a PSD template or actual integration of that theme into WHMCS or Wordpress?"  I don't expect anyone to create new content for the site at that price. What do you charge if  you are able to create content or get directly involved in the site implementation of that template?

```html
<!DOCTYPE html>
<html lang="en">
<head>
<meta charset="utf-8">
<title>Lunetra — Web Hosting</title>
<link href="https://fonts.googleapis.com/css2?family=Open+Sans:wght@300;400;600;700&family=Roboto+Condensed:wght@300;400;700&display=swap" rel="stylesheet">
<style>
:root{
  --brand:#1677b3;
  --brand-dark:#0a5f93;
  --hero-top:#1f8fcb;
  --hero-bottom:#0b6aa5;
  --orange:#f28a1d;
  --orange-text:#f07b1c;
  --shared:#3ab0c8;
  --reseller:#5db94f;
  --vps:#f8b01a;
  --dedicated:#e9544f;
  --ink:#333;
  --muted:#888;
  --light:#f1f1f1;
  --slate:#4a5157;
  --footer:#2f3336;
  --footer-deep:#26292b;
  --white:#fff;
}
*{box-sizing:border-box;margin:0;padding:0}
html,body{width:1200px;height:2483px;overflow:hidden}
body{position:relative;font-family:"Open Sans",Arial,sans-serif;color:var(--ink);background:var(--white)}
.abs{position:absolute}
ul{list-style:none}

/* header */
.site-header{position:absolute;left:0;top:0;width:1200px;height:100px;background:linear-gradient(#fafafa,#ececec)}
.logo{position:absolute;left:100px;top:6px;font-size:70px;font-weight:700;color:var(--brand);letter-spacing:-2px;line-height:1}
.call-pill{position:absolute;left:894px;top:30px;width:206px;height:32px;border-radius:16px 4px 4px 16px;background:linear-gradient(#2f9be0,#1478c4);color:var(--white);font-size:12px;font-weight:700;display:flex;align-items:center;padding-left:8px;gap:8px}
.call-pill .dot{width:24px;height:24px;border-radius:50%;background:var(--white);opacity:.85}
.main-nav{position:absolute;left:0;top:100px;width:1200px;height:46px;background:linear-gradient(#0d7ab7,#075f96);border-top:2px solid #2b95d2}
.main-nav a{position:absolute;top:0;height:44px;line-height:44px;color:var(--white);font-size:13px;font-weight:700;text-decoration:none;transform:translateX(-50%);white-space:nowrap}
.main-nav .active{background:#2b8fcb;padding:0 24px;border-bottom:2px solid #5fc0f0}
.nav-sep{position:absolute;top:12px;width:1px;height:22px;background:#4aa6dc}

/* hero */
.hero{position:absolute;left:0;top:146px;width:1200px;height:499px;background:linear-gradient(var(--hero-top),var(--hero-bottom) 78%,#1b85c2 78%,#0e6ea8)}
.hero h1{position:absolute;left:100px;top:18px;color:var(--white);font-size:35px;font-weight:700;letter-spacing:.5px}
.hero h2{position:absolute;left:100px;top:70px;color:var(--white);font-size:32px;font-weight:300;letter-spacing:.3px}
.hero-list{position:absolute;left:102px;top:136px}
.hero-list li{height:28px;color:var(--white);font-size:13px;font-weight:700;display:flex;align-items:center;gap:9px;white-space:nowrap}
.tick-box{width:14px;height:14px;background:var(--white);border-radius:2px;display:flex;align-items:center;justify-content:center}
.order-btn{position:absolute;left:103px;top:329px;width:210px;height:55px;border-radius:4px;background:linear-gradient(#fbb03b,#ef7d12);border:1px solid #d46d0c;color:var(--white);font-size:21px;font-weight:700;text-align:center;line-height:53px}
.server-art{position:absolute;left:348px;top:252px;width:192px;height:206px;background:linear-gradient(#2a2f36,#0f1216);border-radius:4px}
.video-frame{position:absolute;left:541px;top:135px;width:559px;height:325px;background:var(--white);padding:12px;box-shadow:0 4px 10px rgba(0,0,0,.3)}
.video-screen{width:100%;height:100%;background:#0c0c0c;position:relative}
.play{position:absolute;left:50%;top:50%;width:72px;height:72px;margin:-36px 0 0 -36px;border-radius:50%;background:#2a2a2a}

/* plans */
.plans-title{position:absolute;left:0;top:678px;width:1200px;text-align:center;font-size:28px;font-weight:600;color:#444}
.plans-rule{position:absolute;left:240px;top:725px;width:720px;height:1px;background:linear-gradient(90deg,transparent,#ddd,transparent)}
.plan{position:absolute;top:758px;width:200px;height:381px;color:var(--white);text-align:center;font-family:"Roboto Condensed","Arial Narrow",sans-serif}
.plan.shared{left:119px;background:var(--shared)}
.plan.reseller{left:372px;background:var(--reseller)}
.plan.vps{left:627px;background:var(--vps)}
.plan.dedicated{left:879px;background:var(--dedicated)}
.plan-icon{position:absolute;left:74px;top:32px}
.plan-name{position:absolute;top:92px;width:100%;font-size:25px;font-weight:700}
.plan-type{position:absolute;top:122px;width:100%;font-size:17px;font-weight:300}
.plan-features{position:absolute;top:150px;left:20px;width:160px;font-family:"Open Sans",Arial,sans-serif;font-size:12px}
.plan-features li{height:30px;line-height:30px;border-top:1px solid rgba(255,255,255,.35)}
.plan-features li:first-child{border-top:1px solid rgba(255,255,255,.5)}
.plan-price{position:absolute;top:250px;width:100%;font-size:34px;font-weight:400}
.plan-price sup{font-size:20px;vertical-align:top;position:relative;top:4px}
.plan-per{position:absolute;top:288px;width:100%;font-size:14px;font-weight:300}
.plan-btn{position:absolute;left:50px;top:319px;width:100px;height:30px;background:var(--white);color:#333;font-family:"Open Sans",Arial,sans-serif;font-size:11px;font-weight:700;line-height:30px;border-radius:2px}

/* start or move */
.choose{position:absolute;left:0;top:1183px;width:1200px;height:406px;background:var(--light)}
.choose h2{position:absolute;top:20px;width:100%;text-align:center;font-size:33px;font-weight:400;color:#333}
.choose h2 span{color:#1e88c8}
.choose .intro{position:absolute;left:200px;top:70px;width:800px;text-align:center;font-size:11px;line-height:24px;color:#333}
.path-card{position:absolute;top:134px;width:482px;height:245px;color:var(--white)}
.path-card.new{left:101px;background:linear-gradient(#39a0e6,#1f86cf)}
.path-card.move{left:617px;background:linear-gradient(#545b62,#40464c)}
.path-card h3{position:absolute;left:43px;top:32px;font-size:22px;font-weight:600}
.path-card.new h3 span{color:#0c4b7a}
.path-card.move h3 span{color:#2aa3e6}
.path-card .sub{position:absolute;left:43px;top:70px;font-size:12px}
.path-card ul{position:absolute;top:115px;font-size:12px}
.path-card li{height:27px;display:flex;align-items:center;gap:10px}
.path-card .foot{position:absolute;left:0;bottom:0;width:100%;height:22px;border-top:1px solid rgba(255,255,255,.2);text-align:center;font-size:9px;line-height:22px;color:rgba(255,255,255,.55)}
.swap-circle{position:absolute;left:549px;top:1390px;width:100px;height:100px;border-radius:50%;background:var(--white);border:6px solid var(--light);display:flex;align-items:center;justify-content:center}

/* tabs */
.tab-line{position:absolute;left:100px;top:1729px;width:1000px;height:1px;background:#e6e6e6}
.tab{position:absolute;top:1655px;height:75px;line-height:70px;font-size:20px;text-align:center}
.tab.active{left:100px;width:471px;border-top:3px solid var(--orange);color:var(--brand);font-weight:600;background:var(--white)}
.tab.idle{left:571px;width:529px;color:#444;font-weight:600;background:linear-gradient(#fdfdfd,#f3f3f3)}
.device-art{position:absolute;left:141px;top:1751px;width:356px;height:235px;background:linear-gradient(135deg,#2b3a4a,#0f1419 60%,#3b4a5c);border-radius:6px}
.price-badge{position:absolute;left:410px;top:1740px;width:86px;height:86px;border-radius:50%;background:#222;border:3px solid var(--orange);color:var(--orange);text-align:center;font-size:19px;font-weight:700;line-height:1.05;padding-top:22px}
.price-badge small{font-size:11px}
.offer h3{position:absolute;left:533px;top:1762px;font-size:21px;font-weight:400;color:var(--orange-text)}
.offer-rule{position:absolute;left:533px;top:1802px;width:567px;height:1px;background:#ececec}
.offer p{position:absolute;left:533px;top:1812px;width:560px;font-size:12px;line-height:20px;color:#999}
.offer ul{position:absolute;left:533px;top:1868px;font-size:15px;color:#888}
.offer li{height:25px;display:flex;align-items:center;gap:14px}
.offer li em{font-style:normal;color:var(--orange-text)}
.create-btn{position:absolute;left:535px;top:1961px;width:193px;height:37px;border-radius:19px;background:linear-gradient(#1f86c9,#0d66a6);color:var(--white);font-size:15px;font-weight:700;text-align:center;line-height:37px}

/* trust strip */
.trust{position:absolute;left:0;top:2022px;width:1200px;height:146px;background:#ebebeb;border-top:1px solid #dcdcdc}
.seal{position:absolute;top:46px;height:46px;border-radius:4px;background:#d2d2d2}
.seal.round{border-radius:50%}

/* footer */
.site-footer{position:absolute;left:0;top:2168px;width:1200px;height:273px;background:var(--footer);color:#bbb}
.site-footer h4{position:absolute;top:16px;font-size:14px;font-weight:400;color:#ddd}
.foot-links{position:absolute;top:46px;font-size:11px}
.foot-links li{height:25px;display:flex;align-items:center;gap:8px}
.foot-links li::before{content:"";border-left:4px solid #aaa;border-top:3px solid transparent;border-bottom:3px solid transparent}
.contact{position:absolute;left:659px;font-size:14px;display:flex;align-items:center;gap:12px;color:#ccc}
.foot-logo{position:absolute;left:902px;top:14px;font-size:52px;font-weight:700;color:#8d9094;letter-spacing:-1px;line-height:1}
.follow{position:absolute;left:874px;top:94px;font-size:13px;color:#ccc;display:flex;align-items:center;gap:8px}
.follow i{display:block;width:30px;height:30px;border-radius:4px;background:#6b7178}
.partners{position:absolute;left:109px;top:166px;width:990px;height:63px;background:#3b3f42;display:flex;align-items:center;justify-content:space-around;font-size:22px;font-weight:700;color:#8e9296}
.legal{position:absolute;left:0;top:2441px;width:1200px;height:42px;background:var(--footer-deep);color:#cfcfcf;text-align:center;font-size:10px;line-height:16px;padding-top:5px}
</style>
</head>
<body>

<header class="site-header">
  <div class="logo">lunetra</div>
  <div class="call-pill"><span class="dot"></span>Call 1-800-555-0142 &nbsp;▾</div>
</header>

<nav class="main-nav">
  <a class="active" style="left:137px">Home</a>
  <span class="nav-sep" style="left:190px"></span>
  <a style="left:281px">Domain Name Center</a>
  <span class="nav-sep" style="left:385px"></span>
  <a style="left:501px">Web Site Hosting Center</a>
  <span class="nav-sep" style="left:622px"></span>
  <a style="left:682px">S.E.O Toolkit</a>
  <span class="nav-sep" style="left:780px"></span>
  <a style="left:864px">Support</a>
  <span class="nav-sep" style="left:940px"></span>
  <a style="left:1013px">Client Area</a>
</nav>

<section class="hero">
  <h1>FREE DOMAIN NAME</h1>
  <h2>WITH EVERY NEW HOSTING PACKAGE</h2>
  <div class="server-art" role="img" aria-label="Server towers with glowing blue light bands"></div>
  <ul class="hero-list">
    <li><span class="tick-box"><svg width="10" height="10" viewBox="0 0 11 11"><path d="M1 6l3 3 6-7" fill="none" stroke="#1a80bf" stroke-width="2"/></svg></span>FREE domain name</li>
    <li><span class="tick-box"><svg width="10" height="10" viewBox="0 0 11 11"><path d="M1 6l3 3 6-7" fill="none" stroke="#1a80bf" stroke-width="2"/></svg></span>Oodles of storage &amp; bandwidth</li>
    <li><span class="tick-box"><svg width="10" height="10" viewBox="0 0 11 11"><path d="M1 6l3 3 6-7" fill="none" stroke="#1a80bf" stroke-width="2"/></svg></span>A hoof-click away from a blog</li>
    <li><span class="tick-box"><svg width="10" height="10" viewBox="0 0 11 11"><path d="M1 6l3 3 6-7" fill="none" stroke="#1a80bf" stroke-width="2"/></svg></span>A bullpen full of site templates</li>
    <li><span class="tick-box"><svg width="10" height="10" viewBox="0 0 11 11"><path d="M1 6l3 3 6-7" fill="none" stroke="#1a80bf" stroke-width="2"/></svg></span>Unlimited mailboxes</li>
    <li><span class="tick-box"><svg width="10" height="10" viewBox="0 0 11 11"><path d="M1 6l3 3 6-7" fill="none" stroke="#1a80bf" stroke-width="2"/></svg></span>Powered by 100% Wind Energy</li>
  </ul>
  <div class="order-btn">ORDER NOW</div>
  <div class="video-frame">
    <div class="video-screen">
      <div class="play"><svg width="72" height="72" viewBox="0 0 72 72"><path d="M30 24l18 12-18 12z" fill="#fff"/></svg></div>
    </div>
  </div>
</section>

<h2 class="plans-title">Choose Your Plan</h2>
<div class="plans-rule"></div>

<div class="plan shared">
  <svg class="plan-icon" width="52" height="46" viewBox="0 0 52 46"><path d="M4 12L26 2l22 10z" fill="#fff"/><rect x="4" y="14" width="44" height="8" fill="#fff"/><rect x="4" y="25" width="44" height="8" fill="#fff"/><rect x="4" y="36" width="44" height="8" fill="#fff"/></svg>
  <div class="plan-name">SHARED</div><div class="plan-type">HOSTING</div>
  <ul class="plan-features"><li>FREE PanelDesk</li><li>Raid 10 w/ backups</li><li>Fully Managed Servers</li></ul>
  <div class="plan-price"><sup>$</sup>11.99</div><div class="plan-per">/month</div>
  <div class="plan-btn">VIEW PLANS</div>
</div>
<div class="plan reseller">
  <svg class="plan-icon" width="52" height="46" viewBox="0 0 52 46"><path d="M10 18L26 12l16 6z" fill="#fff"/><rect x="4" y="20" width="44" height="10" fill="#fff"/></svg>
  <div class="plan-name">RESELLER</div><div class="plan-type">HOSTING</div>
  <ul class="plan-features"><li>FREE PanelDesk</li><li>Raid 10 w/ backups</li><li>Fully Managed Servers</li></ul>
  <div class="plan-price"><sup>$</sup>11.99</div><div class="plan-per">/month</div>
  <div class="plan-btn">VIEW PLANS</div>
</div>
<div class="plan vps">
  <svg class="plan-icon" width="52" height="46" viewBox="0 0 52 46"><path d="M4 12L26 4l22 8z" fill="#fff"/><rect x="4" y="14" width="44" height="10" fill="#fff"/><rect x="4" y="27" width="44" height="10" fill="#fff"/></svg>
  <div class="plan-name">VPS</div><div class="plan-type">HOSTING</div>
  <ul class="plan-features"><li>FREE PanelDesk</li><li>Raid 10 w/ backups</li><li>Fully Managed Servers</li></ul>
  <div class="plan-price"><sup>$</sup>39.99</div><div class="plan-per">/month</div>
  <div class="plan-btn">VIEW PLANS</div>
</div>
<div class="plan dedicated">
  <svg class="plan-icon" width="52" height="46" viewBox="0 0 52 46"><path d="M4 10L26 0l22 10z" fill="#fff"/><rect x="4" y="12" width="44" height="7" fill="#fff"/><rect x="4" y="21" width="44" height="7" fill="#fff"/><rect x="4" y="30" width="44" height="7" fill="#fff"/><rect x="4" y="39" width="44" height="7" fill="#fff"/></svg>
  <div class="plan-name">DEDICATED</div><div class="plan-type">HOSTING</div>
  <ul class="plan-features"><li>FREE PanelDesk</li><li>Raid 10 w/ backups</li><li>Fully Managed Servers</li></ul>
  <div class="plan-price"><sup>$</sup>159.49</div><div class="plan-per">/month</div>
  <div class="plan-btn">VIEW PLANS</div>
</div>

<section class="choose">
  <h2>Starting a <span>New Website</span> or Moving from <span>Another Host?</span></h2>
  <p class="intro">Lorem Ipsum is simply dummy text of the printing and typesetting industry. Lorem Ipsum has been the industry's standard dummy text ever since the 1500s, when an unknown printer took a galley of type and scrambled it to make a type specimen book.</p>

  <div class="path-card new">
    <h3>Creating a <span>new website?</span></h3>
    <p class="sub">We offer a variety of options to help you get started</p>
    <svg class="abs" style="left:43px;top:122px" width="190" height="56" viewBox="0 0 190 56">
      <g fill="#fff"><circle cx="24" cy="28" r="16"/><g stroke="#fff" stroke-width="8"><path d="M24 4v48M0 28h48M7 11l34 34M41 11L7 45"/></g></g>
      <circle cx="24" cy="28" r="7" fill="#2790d8"/>
      <path d="M84 28h14M91 21v14" stroke="#fff" stroke-width="4"/>
      <rect x="128" y="6" width="56" height="38" fill="none" stroke="#fff" stroke-width="5"/>
      <rect x="148" y="44" width="16" height="6" fill="#fff"/><rect x="140" y="50" width="32" height="4" fill="#fff"/>
    </svg>
    <ul style="left:260px">
      <li><svg width="12" height="10" viewBox="0 0 12 10"><path d="M1 5l3 3 7-7" fill="none" stroke="#fff" stroke-width="2"/></svg>Website Builder</li>
      <li><svg width="12" height="10" viewBox="0 0 12 10"><path d="M1 5l3 3 7-7" fill="none" stroke="#fff" stroke-width="2"/></svg>300+ Script Auto-Installer</li>
      <li><svg width="12" height="10" viewBox="0 0 12 10"><path d="M1 5l3 3 7-7" fill="none" stroke="#fff" stroke-width="2"/></svg>Request install for free.</li>
    </ul>
    <div class="foot">Click on the box to expand details</div>
  </div>

  <div class="path-card move">
    <h3>Moving from <span>another host?</span></h3>
    <p class="sub">Moving can be a hassle, but it doesn't have to be.</p>
    <svg class="abs" style="left:60px;top:118px" width="200" height="64" viewBox="0 0 200 64">
      <rect x="2" y="8" width="52" height="36" fill="none" stroke="#fff" stroke-width="5"/>
      <rect x="20" y="44" width="16" height="6" fill="#fff"/><rect x="12" y="50" width="32" height="4" fill="#fff"/>
      <path d="M76 32h34M76 32l7-6v12zM110 32l-7-6v12z" fill="#fff" stroke="#fff" stroke-width="3"/>
      <g fill="#fff"><ellipse cx="158" cy="12" rx="26" ry="8"/><rect x="132" y="18" width="52" height="12" rx="4"/><rect x="132" y="33" width="52" height="12" rx="4"/><rect x="132" y="48" width="52" height="12" rx="4"/></g>
    </svg>
    <ul style="left:277px">
      <li><svg width="12" height="10" viewBox="0 0 12 10"><path d="M1 5l3 3 7-7" fill="none" stroke="#fff" stroke-width="2"/></svg><span><b>Free</b> Account Transfer!</span></li>
      <li><svg width="12" height="10" viewBox="0 0 12 10"><path d="M1 5l3 3 7-7" fill="none" stroke="#fff" stroke-width="2"/></svg><span><b>Free</b> Script Transfers!</span></li>
      <li><svg width="12" height="10" viewBox="0 0 12 10"><path d="M1 5l3 3 7-7" fill="none" stroke="#fff" stroke-width="2"/></svg><span><b>Free</b> Database Transfers!</span></li>
    </ul>
    <div class="foot">Click on the box to expand details</div>
  </div>
</section>
<div class="swap-circle">
  <svg width="52" height="44" viewBox="0 0 52 44"><g fill="none" stroke="#1e88c8" stroke-width="5"><path d="M4 13h40M34 4l10 9-10 9"/><path d="M48 31H8M18 22l-10 9 10 9"/></g></svg>
</div>

<div class="tab active">CREATING A NEW WEBSITE?</div>
<div class="tab idle">MOVING FROM ANOTHER HOST?</div>
<div class="tab-line"></div>

<div class="device-art" role="img" aria-label="Website template shown on a desktop monitor, laptop, tablet and phone"></div>
<div class="price-badge">$159.99<br><small>/MO.</small></div>

<div class="offer">
  <h3>We offer a variety of options to help you get started</h3>
  <div class="offer-rule"></div>
  <p>Lorem Ipsum is simply dummy text of the printing and typesetting industry. Lorem Ipsum has been the industry's standard dummy text ever since the 1500s book.</p>
  <ul>
    <li><svg width="16" height="16" viewBox="0 0 16 16"><circle cx="8" cy="8" r="8" fill="#1478b8"/><path d="M4 8l3 3 5-6" fill="none" stroke="#fff" stroke-width="2"/></svg><span>Website Builder <em>(View Demo)</em></span></li>
    <li><svg width="16" height="16" viewBox="0 0 16 16"><circle cx="8" cy="8" r="8" fill="#1478b8"/><path d="M4 8l3 3 5-6" fill="none" stroke="#fff" stroke-width="2"/></svg><span>300+ Script Auto-Installer <em>(Scripts)</em></span></li>
    <li><svg width="16" height="16" viewBox="0 0 16 16"><circle cx="8" cy="8" r="8" fill="#1478b8"/><path d="M4 8l3 3 5-6" fill="none" stroke="#fff" stroke-width="2"/></svg><span>Request us to install any script for free.</span></li>
  </ul>
  <div class="create-btn">CREATE NOW</div>
</div>

<section class="trust">
  <div class="seal" style="left:111px;width:118px"></div>
  <div class="seal" style="left:265px;width:86px"></div>
  <div class="seal" style="left:392px;width:178px"></div>
  <div class="seal round" style="left:622px;width:46px"></div>
  <div class="seal" style="left:728px;width:80px"></div>
  <div class="seal" style="left:844px;width:108px"></div>
  <div class="seal" style="left:960px;width:128px"></div>
</section>

<footer class="site-footer">
  <h4 style="left:108px">Company</h4>
  <h4 style="left:453px">Our Product</h4>
  <h4 style="left:659px">Get in Touch</h4>
  <ul class="foot-links" style="left:114px"><li>Home</li><li>About Us</li><li>Products</li></ul>
  <ul class="foot-links" style="left:276px"><li>News</li><li>Our Clients</li><li>Contact Us</li></ul>
  <ul class="foot-links" style="left:460px"><li>Selvbetjening</li><li>Digital mail</li><li>Virtual desktops</li></ul>
  <div class="contact" style="top:52px"><svg width="20" height="20" viewBox="0 0 20 20"><circle cx="10" cy="10" r="8" fill="none" stroke="#ccc" stroke-width="2"/><path d="M7 6l2 2-1 2 2 2 2-1 2 2-2 2c-4 0-8-4-8-8z" fill="#ccc"/></svg>000 000 0000</div>
  <div class="contact" style="top:86px"><svg width="20" height="14" viewBox="0 0 20 14"><rect x="1" y="1" width="18" height="12" fill="none" stroke="#ccc" stroke-width="2"/><path d="M1 1l9 7 9-7" fill="none" stroke="#ccc" stroke-width="2"/></svg>info@lunetra.com</div>
  <div class="foot-logo">lunetra</div>
  <div class="follow">Follow us:&nbsp;<i></i><i></i><i></i><i></i></div>
  <div class="partners"><span>Quelbrook</span><span>Tarnvik</span><span>Holmfast</span><span>Ostrel</span><span>Brevant</span><span>Caldmere</span></div>
</footer>

<div class="legal">
  Terms of Use -- Dispute Policy -- Disclaimer -- Privacy Policy -- Refund Policy -- Refund Policy -- Lunetra Newsletter<br>
  Copyright © 2010 Lunetra.com. All Rights Reserved.
</div>

</body>
</html>
```